Wine Label

I need a label for my home made red wine. I name it Kestravin Reserve, I want a vintage design with an "Ouroboros encircled around a Sowilo rune" incorporated in the design

```html
<!DOCTYPE html>
<html lang="en">
<head>
<meta charset="utf-8">
<title>Kestravin Reserve – Wine Label</title>
<link rel="stylesheet" href="https://fonts.googleapis.com/css2?family=Metamorphous&display=swap">
<style>
  :root {
    --canvas-bg: #ffffff;
    --gold-dark: #9a6c12;
    --gold-mid: #c29532;
    --gold-light: #d6ad4f;
    --gold-ink: #c9a034;
    --gold-deep: #a7801f;
    --panel-black: #151314;
    --panel-edge: #3a3530;
  }
  * { box-sizing: border-box; margin: 0; padding: 0; }
  html, body {
    width: 1200px;
    height: 1200px;
    overflow: hidden;
    background: var(--canvas-bg);
  }
  .canvas {
    position: relative;
    width: 1200px;
    height: 1200px;
  }
  .label {
    position: absolute;
    left: 225px;
    top: 100px;
    width: 750px;
    height: 1000px;
    background: linear-gradient(90deg, var(--gold-dark) 0%, var(--gold-mid) 55%, var(--gold-light) 100%);
  }
  .label-frame {
    position: absolute;
    inset: 0;
    width: 750px;
    height: 1000px;
  }
  .brand-mark {
    position: absolute;
    left: 330px;
    top: 140px;
    width: 90px;
    height: 90px;
    border-radius: 50%;
    background: var(--gold-ink);
  }
  .wine-name {
    position: absolute;
    left: 0;
    width: 750px;
    text-align: center;
    font-family: "Metamorphous", serif;
    color: var(--gold-ink);
    font-weight: 400;
    line-height: 1;
    white-space: nowrap;
  }
  .wine-name__main {
    top: 335px;
    font-size: 80px;
    letter-spacing: 2px;
  }
  .wine-name__sub {
    top: 488px;
    font-size: 54px;
    letter-spacing: 4px;
  }
  .knot-ornament {
    position: absolute;
    left: 150px;
    top: 580px;
    width: 450px;
    height: 240px;
  }
  .foot-ornament {
    position: absolute;
    left: 318px;
    top: 872px;
    width: 114px;
    height: 18px;
    border-radius: 9px;
    background: var(--gold-deep);
  }
</style>
</head>
<body>
<main class="canvas">
  <section class="label">
    <svg class="label-frame" viewBox="0 0 750 1000" aria-hidden="true">
      <path class="label-frame__panel"
        d="M375,32 C345,32 335,48 322,62 C300,72 250,80 200,82 L200,100 L175,100 L175,120 L150,120 L150,140 C90,160 30,200 18,260 L18,800 C18,860 80,880 170,880 C250,880 300,905 330,935 C350,960 400,960 420,935 C450,905 500,880 580,880 C670,880 732,860 732,800 L732,260 C720,200 660,160 600,140 L600,120 L575,120 L575,100 L550,100 L550,82 C500,80 450,72 428,62 C415,48 405,32 375,32 Z"
        fill="var(--panel-black)" stroke="var(--panel-edge)" stroke-width="3"/>
      <path class="label-frame__inner-rule"
        transform="translate(375 500) scale(0.93 0.925) translate(-375 -500)"
        d="M375,32 C345,32 335,48 322,62 C300,72 250,80 200,82 L200,100 L175,100 L175,120 L150,120 L150,140 C90,160 30,200 18,260 L18,800 C18,860 80,880 170,880 C250,880 300,905 330,935 C350,960 400,960 420,935 C450,905 500,880 580,880 C670,880 732,860 732,800 L732,260 C720,200 660,160 600,140 L600,120 L575,120 L575,100 L550,100 L550,82 C500,80 450,72 428,62 C415,48 405,32 375,32 Z"
        fill="none" stroke="var(--gold-ink)" stroke-width="3" vector-effect="non-scaling-stroke"/>
    </svg>

    <div class="brand-mark" aria-hidden="true"></div>
    <h1 class="wine-name wine-name__main">KESTRAVIN</h1>
    <p class="wine-name wine-name__sub">RESERVE</p>

    <svg class="knot-ornament" viewBox="0 0 450 240" role="img" aria-label="Gold interlaced knotwork ornament flanked by two stylised serpent heads">
      <defs>
        <linearGradient id="ornament-tone" x1="0" y1="0" x2="0" y2="1">
          <stop offset="0" stop-color="#c9a034"/>
          <stop offset="1" stop-color="#a7801f"/>
        </linearGradient>
      </defs>
      <rect x="0" y="0" width="450" height="240" rx="36" fill="url(#ornament-tone)" opacity="0.9"/>
    </svg>
    <div class="foot-ornament" role="img" aria-label="Small gold flourish ornament"></div>
  </section>
</main>
</body>
</html>
```